Business Card Design for digital storytelling business

I need a business card for a workshop/consulting/coaching business.

Company Name: The Bright Harbor

Tagline: New Ways to Keep Old Family Memories

What we do: Through workshops, webinars, and coaching we teach you how to capture, tell and share your important memories and stories using readily available digital tools. We will help you tell your life story in a format to share with your family now and in the future.
Updates

I just received a toll free number that I would like included on the designs. If the addition of a phone number would significantly alter your design, please submit an altered version. The number is 877-512-6098

Target Market(s)

Adults in US between ages of 35-70 interested in capturing, preserving and sharing memories and life stories in a digital format.
Could include the following:

-People touched by illness or tragedy who need to tell their own or a loved one's life story
-Grandparents wanting to share stories and wisdom with grandchildren living far away
-People with aging parents who want to capture their stories in a format to pass on to their children
-Alzheimer's patients and their families
-People wanting to transfer analog photos to digital; or wanting to organize digital photos into something that tells a story

Industry/Entity Type

Digital

Requirements
Must have
• Must include business name, logo, tagline

Contact information (see file)
Social media information

Fonts easily readable by aging eyes. Good contrast.

Nice to have
• Color preferences: blue, green, yellow/gold
Blue denotes the calm, non-pressured way that I teach. It is for the healing that comes from telling your story. It represents time and space that are bridged in the digital environment.
Green is for growth, the future, the family tree, Vines that grow and branch and connect the generations and our hearts.
Yellow/gold is for the legacy of wisdom in our lives and stories. It is for the light of truth we bring to the world by sharing our stories.
Should not have
• No old-style, script fonts.
No Times New Roman

```html
<!DOCTYPE html>
<html lang="en">
<head>
<meta charset="utf-8">
<title>The Bright Harbor – Business Card</title>
<link href="https://fonts.googleapis.com/css2?family=Source+Sans+3:wght@400;600&family=Marcellus&family=Dancing+Script:wght@500&display=swap" rel="stylesheet">
<style>
  :root {
    --navy: #253b6c;
    --navy-light: #324a7a;
    --white: #ffffff;
    --ink: #1d1d1f;
    --backdrop: #e6e7ea;
  }
  * { margin: 0; padding: 0; box-sizing: border-box; }
  html, body {
    width: 1200px; height: 602px; overflow: hidden;
    background: var(--backdrop);
    font-family: "Source Sans 3", "Source Sans Pro", sans-serif;
  }
  .card {
    position: absolute; top: 153px;
    width: 467px; height: 277px;
    border-radius: 17px; overflow: hidden;
  }
  /* Front */
  .card-front {
    left: 119px;
    background: linear-gradient(180deg, var(--navy-light) 0%, var(--navy) 55%);
    color: var(--white);
  }
  .brand-mark {
    position: absolute; left: 50%; top: 34px;
    width: 74px; height: 74px; margin-left: -37px;
    border-radius: 50%; border: 3px solid var(--white);
  }
  .brand-name {
    position: absolute; left: 0; right: 0; top: 132px;
    text-align: center; font-size: 33px; font-weight: 400;
    letter-spacing: 0.3px;
  }
  .tagline {
    position: absolute; left: 0; right: 0; top: 177px;
    text-align: center; font-family: "Marcellus", serif;
    font-size: 13px; letter-spacing: 0.6px;
  }
  .social { position: absolute; top: 210px; width: 140px; text-align: center; }
  .social-dot {
    display: block; width: 21px; height: 21px; margin: 0 auto 2px;
    border-radius: 50%; background: var(--white);
  }
  .social-handle { font-size: 14px; }
  .social-1 { left: 36px; }
  .social-2 { left: 171px; }
  .social-3 { left: 302px; }
  /* Back */
  .card-back { left: 638px; background: var(--white); color: var(--ink); }
  .name-rule {
    position: absolute; top: 123px; height: 2px; background: var(--ink);
  }
  .name-rule-left { left: 0; width: 115px; }
  .name-rule-right { right: 0; width: 112px; }
  .person-name {
    position: absolute; left: 0; right: 0; top: 96px;
    text-align: center; font-family: "Dancing Script", cursive;
    font-size: 42px; font-weight: 500; line-height: 1;
  }
  .person-title {
    position: absolute; left: 0; right: 0; top: 134px;
    text-align: center; font-size: 19px; letter-spacing: 0.5px; line-height: 1;
    padding-left: 14px;
  }
  .contact { position: absolute; top: 192px; font-size: 14px; line-height: 17px; }
  .contact-postal { left: 18px; }
  .contact-online { right: 16px; text-align: right; }
  .phone-band {
    position: absolute; left: 0; right: 0; bottom: 0; height: 43px;
    background: var(--navy); color: var(--white);
    display: flex; align-items: center; justify-content: center;
    font-size: 15px; font-weight: 600;
  }
</style>
</head>
<body>
  <section class="card card-front" aria-label="Card front">
    <span class="brand-mark"></span>
    <h1 class="brand-name">The Bright Harbor</h1>
    <p class="tagline">NEW WAYS TO KEEP OLD FAMILY MEMORIES</p>
    <div class="social social-1"><span class="social-dot"></span><span class="social-handle">TheBrightHarbor</span></div>
    <div class="social social-2"><span class="social-dot"></span><span class="social-handle">@BrightHarbor</span></div>
    <div class="social social-3"><span class="social-dot"></span><span class="social-handle">BrightHarborTales</span></div>
  </section>

  <section class="card card-back" aria-label="Card back">
    <span class="name-rule name-rule-left"></span>
    <span class="name-rule name-rule-right"></span>
    <h2 class="person-name">Helen Marsh</h2>
    <p class="person-title">FOUNDER</p>
    <p class="contact contact-postal">PO Box 218<br>Westbrook, CT 06498</p>
    <p class="contact contact-online">helen@thebrightharbor.com<br>www.thebrightharbor.com</p>
    <div class="phone-band">Toll Free: 877-512-6098</div>
  </section>
</body>
</html>
```